Plumbing & Heating company

A leaflet containing -

Company name - Brackenfold Plumbing Solutions
logo
Mobile number - 07700 914226
Landline - 01632 870512
Email - Info@brackenfoldplumbing.example.co.uk
website - Brackenfold-plumbing.example.co.uk
Social media logos - pixgram, Chatterly

services we offer

- Boiler replacements (free quote)
- General plumbing & heating
- Tap replacements
- 1st & 2nd
- New builds & Extensions
- Cylinder replcemets

```html
<!DOCTYPE html>
<html lang="en">
<head>
<meta charset="utf-8">
<title>Brackenfold Plumbing Solutions – Leaflet</title>
<link rel="stylesheet" href="https://fonts.googleapis.com/css2?family=Oswald:wght@500;600&family=Montserrat:wght@600;700&family=Roboto+Condensed:wght@400;500&display=swap">
<style>
  :root {
    --orange: #f47a2e;
    --blue: #2f86c2;
    --blue-text: #2d7fbd;
    --steel: #34586c;
    --steel-dark: #22404f;
    --white: #ffffff;
    --page: #eeeeee;
  }
  * { box-sizing: border-box; margin: 0; padding: 0; }
  html, body { width: 1200px; height: 1000px; overflow: hidden; background: var(--page); }
  .leaflet {
    position: absolute; left: 267px; top: 30px;
    width: 665px; height: 940px; overflow: hidden;
    background: var(--white);
    box-shadow: 0 6px 24px rgba(0,0,0,.18);
  }
  .leaflet-shapes { position: absolute; inset: 0; }
  .brand-tab {
    position: absolute; left: 17px; top: 0; width: 127px; height: 108px;
    display: flex; flex-direction: column; align-items: center; justify-content: center;
    font-family: "Oswald", sans-serif; font-weight: 600; color: var(--blue);
    text-align: center; line-height: 1.05;
  }
  .brand-tab .brand-name { font-size: 19px; letter-spacing: .5px; text-transform: uppercase; }
  .brand-tab .brand-sub { font-size: 8.5px; letter-spacing: .6px; text-transform: uppercase; }
  .title { position: absolute; left: 198px; top: 26px; color: var(--white); }
  .title-line { display: block; font-family: "Oswald", sans-serif; font-weight: 500;
    font-size: 52px; line-height: 54px; letter-spacing: 2px; text-transform: uppercase; }
  .title-line.accent { color: var(--orange); }
  .title-sub { display: block; font-family: "Montserrat", sans-serif; font-weight: 600;
    font-size: 31px; letter-spacing: 2px; margin-top: 2px; text-transform: uppercase; }
  .services { position: absolute; left: 42px; top: 442px; }
  .services h2 { font-family: "Oswald", sans-serif; font-weight: 600; font-size: 44px;
    letter-spacing: 2px; color: var(--orange); line-height: 1; margin-bottom: 14px; }
  .service-list { list-style: none; }
  .service-list li { display: flex; align-items: center; height: 40px;
    font-family: "Roboto Condensed", sans-serif; font-weight: 500; font-size: 28px; color: var(--blue-text); }
  .tick { width: 38px; height: 30px; margin-right: 10px; flex: none; }
  .contact-box { position: absolute; left: 442px; top: 672px; width: 223px; height: 63px;
    background: var(--blue); padding: 5px 0 0 22px; }
  .contact-line { display: flex; align-items: center; height: 27px;
    font-family: "Montserrat", sans-serif; font-weight: 700; font-size: 18px; color: var(--white); letter-spacing: .5px; }
  .contact-line svg { width: 24px; height: 24px; margin-right: 8px; }
  .footer-links { position: absolute; top: 862px; font-family: "Montserrat", sans-serif;
    font-weight: 600; font-size: 13.5px; color: var(--white); }
  .footer-links.left { left: 42px; }
  .footer-links.right { left: 436px; }
  .footer-links li { list-style: none; display: flex; align-items: center; height: 33px; }
  .footer-links svg { width: 20px; height: 20px; margin-right: 7px; flex: none; }
</style>
</head>
<body>
<main class="leaflet">
  <svg class="leaflet-shapes" viewBox="0 0 665 940" aria-hidden="false">
    <defs>
      <linearGradient id="pipeworkTone" x1="0" y1="0" x2="1" y2="1">
        <stop offset="0" stop-color="#3f6579"/><stop offset="1" stop-color="#22404f"/>
      </linearGradient>
      <linearGradient id="cupboardTone" x1="0" y1="0" x2="0" y2="1">
        <stop offset="0" stop-color="#d9b48e"/><stop offset="1" stop-color="#b88c63"/>
      </linearGradient>
      <linearGradient id="copperTone" x1="0" y1="0" x2="1" y2="1">
        <stop offset="0" stop-color="#a98e6c"/><stop offset="1" stop-color="#6f6a62"/>
      </linearGradient>
      <linearGradient id="cylinderTone" x1="0" y1="0" x2="1" y2="0">
        <stop offset="0" stop-color="#f2f2f2"/><stop offset="1" stop-color="#cfd3d6"/>
      </linearGradient>
    </defs>
    <rect class="header-photo" x="0" y="0" width="665" height="420" fill="url(#pipeworkTone)" role="img" aria-label="Photo of insulated heating pipework and zone valves"/>
    <path class="wave-orange" d="M0,350 C120,210 380,250 665,170 L665,940 L0,940Z" fill="var(--orange)"/>
    <path class="wave-blue" d="M0,362 C120,222 380,262 665,182 L665,940 L0,940Z" fill="var(--blue)"/>
    <path class="wave-white" d="M0,372 C120,232 380,272 665,194 L665,940 L0,940Z" fill="var(--white)"/>
    <polygon class="brand-tab-shape" points="17,0 144,0 144,108 80,135 17,108" fill="var(--white)"/>
    <g class="hex-gallery" stroke="var(--orange)" stroke-width="8" stroke-linejoin="round">
      <polygon points="153,185 242,238 242,344 153,397 64,344 64,238" fill="url(#cupboardTone)" role="img" aria-label="Photo of a wall-hung boiler installed in a cupboard"/>
      <polygon points="332,200 421,253 421,359 332,412 243,359 243,253" fill="url(#copperTone)" role="img" aria-label="Photo of copper pipework run through floor joists"/>
      <polygon points="511,208 600,261 600,367 511,420 422,367 422,261" fill="url(#cylinderTone)" role="img" aria-label="Photo of a hot water cylinder and boiler installation"/>
    </g>
    <path class="footer-blue" d="M0,858 C90,800 170,788 240,795 C330,804 380,858 470,853 C560,848 620,800 665,768 L665,940 L0,940Z" fill="var(--blue)"/>
    <path class="footer-orange" d="M0,872 C90,814 170,802 240,809 C330,818 380,872 470,867 C560,862 620,814 665,782 L665,940 L0,940Z" fill="var(--orange)"/>
  </svg>

  <div class="brand-tab">
    <span class="brand-name">Brackenfold</span>
    <span class="brand-sub">Plumbing Solutions</span>
  </div>

  <h1 class="title">
    <span class="title-line">Brackenfold</span>
    <span class="title-line accent">Plumbing</span>
    <span class="title-sub">Solutions</span>
  </h1>

  <section class="services">
    <h2>OUR SERVICES</h2>
    <ul class="service-list">
      <li><svg class="tick" viewBox="0 0 38 30"><rect x="2" y="6" width="22" height="22" fill="none" stroke="var(--orange)" stroke-width="3"/><path d="M7,15 L13,22 L35,3" fill="none" stroke="var(--orange)" stroke-width="3.5"/></svg>Boiler&nbsp; Replacement ( Free Quote)</li>
      <li><svg class="tick" viewBox="0 0 38 30"><rect x="2" y="6" width="22" height="22" fill="none" stroke="var(--orange)" stroke-width="3"/><path d="M7,15 L13,22 L35,3" fill="none" stroke="var(--orange)" stroke-width="3.5"/></svg>General Plumbing &amp; Heating</li>
      <li><svg class="tick" viewBox="0 0 38 30"><rect x="2" y="6" width="22" height="22" fill="none" stroke="var(--orange)" stroke-width="3"/><path d="M7,15 L13,22 L35,3" fill="none" stroke="var(--orange)" stroke-width="3.5"/></svg>Tap Replacements</li>
      <li><svg class="tick" viewBox="0 0 38 30"><rect x="2" y="6" width="22" height="22" fill="none" stroke="var(--orange)" stroke-width="3"/><path d="M7,15 L13,22 L35,3" fill="none" stroke="var(--orange)" stroke-width="3.5"/></svg>1st &amp; 2nd</li>
      <li><svg class="tick" viewBox="0 0 38 30"><rect x="2" y="6" width="22" height="22" fill="none" stroke="var(--orange)" stroke-width="3"/><path d="M7,15 L13,22 L35,3" fill="none" stroke="var(--orange)" stroke-width="3.5"/></svg>New Builds &amp; Extensions</li>
      <li><svg class="tick" viewBox="0 0 38 30"><rect x="2" y="6" width="22" height="22" fill="none" stroke="var(--orange)" stroke-width="3"/><path d="M7,15 L13,22 L35,3" fill="none" stroke="var(--orange)" stroke-width="3.5"/></svg>Cylinder Replcements</li>
    </ul>
  </section>

  <div class="contact-box">
    <div class="contact-line"><svg viewBox="0 0 24 24"><circle cx="12" cy="12" r="10.5" fill="none" stroke="#fff" stroke-width="1.8"/><path d="M8.5,6.5 L10.5,9 L9.5,10.5 C10.3,12 11.8,13.6 13.5,14.5 L15,13.5 L17.5,15.5 L16.5,17.5 C12,17.5 6.5,12 6.5,7.5Z" fill="#fff"/></svg>07700 914226</div>
    <div class="contact-line"><svg viewBox="0 0 24 24"><circle cx="12" cy="12" r="10.5" fill="none" stroke="#fff" stroke-width="1.8"/><path d="M6,10 C6,7 18,7 18,10 L16,10.5 L15,9 L9,9 L8,10.5Z M8,11.5 L16,11.5 L17,17 L7,17Z" fill="#fff"/><circle cx="12" cy="14" r="1.6" fill="var(--blue)"/></svg>01632 870512</div>
  </div>

  <ul class="footer-links left">
    <li><svg viewBox="0 0 20 20"><circle cx="10" cy="10" r="9" fill="none" stroke="#fff" stroke-width="1.5"/><rect x="5.5" y="6.5" width="9" height="7" fill="none" stroke="#fff" stroke-width="1.3"/><path d="M5.5,6.5 L10,10.5 L14.5,6.5" fill="none" stroke="#fff" stroke-width="1.3"/></svg>info@brackenfoldplumbing.example.co.uk</li>
    <li><svg viewBox="0 0 20 20"><circle cx="10" cy="10" r="9" fill="none" stroke="#fff" stroke-width="1.5"/><path d="M8,5.5 L8,14 L10,12 L11.5,15 L12.8,14.4 L11.3,11.4 L14,11.2Z" fill="#fff"/></svg>www.brackenfold-plumbing.example.co.uk</li>
  </ul>
  <ul class="footer-links right">
    <li><svg viewBox="0 0 20 20"><circle cx="10" cy="10" r="8" fill="none" stroke="#fff" stroke-width="1.6"/></svg>www.pixgram.example.com</li>
    <li><svg viewBox="0 0 20 20"><circle cx="10" cy="10" r="8" fill="none" stroke="#fff" stroke-width="1.6"/></svg>www.chatterly.example.com</li>
  </ul>
</main>
</body>
</html>
```